Tranquil Pathway Business Card

Logo attached. (will be printing onto thick white/off white textured card)

Double sided business card for two Therapists working at Tranquil Pathway.

Require one design, but with different name and mobile numbers on each card.

Target Market(s)

Medical, Health

Industry/Entity Type

Business

Contact Information for Business Card

Need one business card design, but a separate card for each person - Colin Marchetti and Marieke de Boeckx.

FRONT OF CARD

Logo

Name (Colin Marchetti on one card, Marieke de Boeckx on the other)
Professional Clinical Hypnotherapist

Consulting Rooms (Near Lindqvist Hospital)
482 Brackenfield Road
Dunmore VIC 3987

Colin@TranquilPathway.example.au OR Marieke@TranquilPathway.example.au

Mobile: 0455 872 604 (for Colin) OR
Mobile: 0467 290 518 (for Marieke)

BACK OF CARD

Logo

Website: www.TranquilPathway.example.au

Phone: 1300 958 471

Requirements
Must have
• Text and logo only. No additiional graphics.

```html
<!DOCTYPE html>
<html lang="en">
<head>
<meta charset="utf-8">
<title>Tranquil Pathway Business Card</title>
<link rel="stylesheet" href="https://fonts.googleapis.com/css2?family=Arimo:wght@400;700&family=Josefin+Sans:wght@300;400&display=swap">
<style>
  :root {
    --navy: #232a62;
    --orange: #f0913a;
    --grey-text: #555659;
    --icon: #5e5f61;
    --mark-front: #d7d9de;
    --mark-back: #e4f5fc;
    --front-light: #ffffff;
    --front-edge: #e3e3e3;
    --back-light: #b9e5f8;
    --back-edge: #1fb3ee;
    --page: #ffffff;
  }
  * { box-sizing: border-box; margin: 0; padding: 0; }
  html, body {
    width: 924px; height: 1200px; overflow: hidden;
    background: var(--page);
    font-family: "Arimo", Arial, sans-serif;
  }
  .card {
    position: absolute; left: 0; width: 897px; height: 538px;
    box-shadow: 14px 12px 12px rgba(0,0,0,0.28);
  }
  .card-front {
    top: 0;
    background: radial-gradient(ellipse at 45% 45%, var(--front-light) 0%, #f6f6f6 45%, var(--front-edge) 100%);
  }
  .card-back {
    top: 625px;
    background: radial-gradient(ellipse at 50% 45%, var(--back-light) 0%, #7fd2f4 45%, var(--back-edge) 100%);
  }
  .brand { position: absolute; display: flex; align-items: center; }
  .brand-mark { border-radius: 50%; flex: none; }
  .brand-name {
    color: var(--navy); font-weight: 700; text-transform: uppercase;
    line-height: 1.05; letter-spacing: 1px;
  }
  .card-front .brand { left: 392px; top: 34px; }
  .card-front .brand-mark { width: 138px; height: 138px; background: var(--mark-front); }
  .card-front .brand-name { font-size: 40px; margin-left: 36px; }
  .card-back .brand { left: 205px; top: 168px; }
  .card-back .brand-mark { width: 154px; height: 154px; background: var(--mark-back); }
  .card-back .brand-name { font-size: 44px; margin-left: 36px; }

  .person { position: absolute; left: 72px; top: 240px; }
  .person-name {
    font-family: "Josefin Sans", sans-serif; font-weight: 300;
    font-size: 57px; color: var(--navy); line-height: 1;
  }
  .person-role {
    font-family: "Josefin Sans", sans-serif; font-weight: 300;
    font-size: 26px; color: var(--orange); margin-top: 8px; margin-left: -7px;
  }
  .contact { position: absolute; right: 46px; top: 352px; text-align: right; color: var(--grey-text); }
  .contact-row { display: flex; justify-content: flex-end; align-items: flex-start; }
  .contact-row svg { flex: none; margin-left: 14px; }
  .mobile { font-size: 34px; line-height: 1; }
  .email { font-size: 20px; margin-top: 16px; }
  .address { font-size: 20px; line-height: 23px; margin-top: 10px; }

  .back-contact {
    position: absolute; left: 0; width: 897px; top: 1074px;
    text-align: center; color: var(--navy); font-size: 24px; line-height: 30px;
  }
</style>
</head>
<body>
  <section class="card card-front">
    <div class="brand">
      <span class="brand-mark"></span>
      <span class="brand-name">Tranquil<br>Pathway</span>
    </div>
    <div class="person">
      <h1 class="person-name">Colin Marchetti</h1>
      <p class="person-role">Professional Clinical Hypnotherapist</p>
    </div>
    <div class="contact">
      <div class="contact-row">
        <span class="mobile">0455 872 604</span>
        <svg width="32" height="32" viewBox="0 0 32 32" aria-hidden="true">
          <circle cx="16" cy="16" r="14" fill="none" stroke="var(--icon)" stroke-width="2.4"/>
          <path d="M11 9 l3 0 l1.5 4 l-2 1.5 c1 2.2 2.5 3.7 4.5 4.5 l1.5-2 l4 1.5 l0 3 c-7 1-14-6-12.5-12.5z" fill="var(--icon)"/>
        </svg>
      </div>
      <div class="contact-row email">
        <span>Colin@TranquilPathway.example.au</span>
        <svg width="32" height="20" viewBox="0 0 32 20" aria-hidden="true">
          <rect x="3" y="2" width="26" height="16" fill="var(--icon)"/>
          <path d="M3 2 L16 12 L29 2" fill="none" stroke="#f2f2f2" stroke-width="1.6"/>
        </svg>
      </div>
      <div class="contact-row address">
        <span>Consulting Rooms (Near Lindqvist Hospital)<br>482 Brackenfield Road<br>Dunmore VIC 3987</span>
        <svg width="32" height="32" viewBox="0 0 32 32" aria-hidden="true">
          <path d="M16 2 L30 9 L2 9 Z" fill="var(--icon)"/>
          <rect x="4" y="11" width="24" height="19" fill="var(--icon)"/>
          <rect x="15" y="16" width="9" height="7" fill="#f0f0f0"/>
          <path d="M19.5 16 v7 M15 19.5 h9" stroke="var(--icon)" stroke-width="1.4"/>
        </svg>
      </div>
    </div>
  </section>

  <section class="card card-back">
    <div class="brand">
      <span class="brand-mark"></span>
      <span class="brand-name">Tranquil<br>Pathway</span>
    </div>
  </section>
  <div class="back-contact">
    <p>www.TranquilPathway.example.au</p>
    <p>Phone : 1300 958 471</p>
  </div>
</body>
</html>
```